Kestrel Summit 2019 Enemies of the End-Times Church Flyer

We want a church conference flyer designed. We are looking for a professional, yet catchy design that uses our brand colors and logo creatively while communicating key information of the event effectively. <br/>The flyer must include all of the following:<br/>Title: Kestrel Summit 2019<br/>Topic: The Enemies of The End-Times Church <br/>Subtitles: <br/> -How the antichrist raises an army by social behavior engineering. <br/>-How the architects of modern social constructs escaped the church's radar. <br/>-The Holy Spirit's end-times agenda:<br/> The Knock-Out Punch!<br/>Speaker: Prophet Marcus Toliver <br/>Dates/time: December 27, 28 & 29 at 6pm<br/>Location: Halvorn Community Center <br/> 241 Pellham Street <br/> Portland, ME 04102<br/>Contact info: phone: 207-555-0148 <br/>email: contact@brookmeadow.example <br/> www.vutel.example<br/>*The flyer must also include a picture of the speaker and our Vutel logo <br/>Thanks, we look forward to seeing what you come up with!

Colors

Designer to choose colors to be used in the design.

Requirements
Must have
• The flyer must include all of the following:
• Title: Kestrel Summit 2019
• Topic: The Enemies of The End-Times Church
• Subtitles:
• -How the antichrist raises an army by social behavior engineering.
• -How the architects of modern social constructs escaped the church's radar.
• -The Holy Spirit's end-times agenda:
• The Knock-Out Punch!
• Speaker: Prophet Marcus Toliver
• Dates/time: December 27, 28 & 29 at 6pm
• Location: Halvorn Community Center
• 241 Pellham Street
• Portland, ME 04102
• Contact info: phone: 207-555-0148
• email: contact@brookmeadow.example
• www.vutel.example
• *The flyer must also include a picture of the speaker and our Vutel logo
Should not have
• Pictures of crosses or church buildings

```html
<!DOCTYPE html>
<html lang="en">
<head>
<meta charset="utf-8">
<title>Kestrel Summit 2019 – Flyer</title>
<link rel="stylesheet" href="https://fonts.googleapis.com/css2?family=Montserrat:wght@600;700;800;900&family=Oswald:wght@600;700&display=swap">
<style>
  :root {
    --navy-deep: #0d1726;
    --navy: #12253d;
    --blue: #15466f;
    --orange: #f7941d;
    --white: #ffffff;
    --rule: rgba(255,255,255,0.75);
  }
  * { margin: 0; padding: 0; box-sizing: border-box; }
  html, body { width: 900px; height: 1200px; overflow: hidden; background: var(--navy-deep); }
  .flyer {
    position: relative; width: 900px; height: 1200px; overflow: hidden;
    font-family: "Montserrat", sans-serif; color: var(--white);
    background: var(--navy-deep);
  }
  .backdrop { position: absolute; inset: 0; }

  .brand { position: absolute; left: 72px; top: 112px; display: flex; align-items: center; gap: 14px; }
  .brand-mark { width: 28px; height: 28px; border-radius: 50%; background: var(--orange); }
  .brand-name { font-weight: 700; font-size: 76px; letter-spacing: 2px; line-height: 1; color: var(--white); }
  .brand-tagline {
    position: absolute; left: 92px; top: 194px; line-height: 1;
    font-weight: 600; font-size: 17px; letter-spacing: 1px; color: var(--orange);
  }

  .title { position: absolute; inset: 0; font-weight: 900; line-height: 1; pointer-events: none; }
  .title-line { position: absolute; left: 54px; color: var(--white); font-size: 88px; letter-spacing: -1px; }
  .title-line.first { top: 258px; }
  .title-line.second { top: 338px; }
  .title-year { position: absolute; left: 470px; top: 203px; color: var(--orange); font-size: 134px; letter-spacing: -2px; }
  .topic { position: absolute; left: 60px; top: 428px; line-height: 1.1; font-weight: 800; font-size: 31px; color: var(--orange); white-space: nowrap; }

  .speaker-photo { position: absolute; left: 62px; top: 480px; width: 400px; height: 430px; }

  .ribbon { position: absolute; transform: rotate(-10deg); transform-origin: left center; font-family: "Oswald", sans-serif; font-weight: 700; text-transform: uppercase; white-space: nowrap; }
  .ribbon-role { left: 80px; top: 880px; background: var(--orange); color: var(--navy-deep); font-size: 40px; padding: 0 16px; line-height: 58px; }
  .ribbon-name { left: 114px; top: 962px; background: var(--navy); color: var(--white); font-size: 44px; padding: 0 16px; line-height: 70px; border-left: 6px solid var(--orange); }

  .topics { position: absolute; right: 55px; top: 560px; width: 350px; text-align: right; }
  .topic-item { font-weight: 700; font-size: 21px; line-height: 28px; padding: 0 0 12px; border-bottom: 3px solid var(--rule); margin-bottom: 12px; }
  .topic-item.small { font-size: 18px; line-height: 24px; }
  .topic-punch { display: block; color: var(--orange); font-size: 27px; line-height: 36px; font-weight: 800; }

  .event-info { position: absolute; right: 55px; top: 934px; width: 480px; text-align: right; white-space: nowrap; }
  .event-dates { font-weight: 800; font-size: 30px; line-height: 36px; color: var(--orange); }
  .event-time { font-weight: 800; font-size: 30px; line-height: 36px; padding-bottom: 10px; border-bottom: 3px solid var(--rule); margin: 0 0 10px 120px; }
  .venue-name { font-weight: 800; font-size: 30px; line-height: 36px; color: var(--orange); }
  .venue-address { font-weight: 700; font-size: 20px; line-height: 26px; }

  .contact-bar {
    position: absolute; left: 0; bottom: 0; width: 900px; height: 68px; background: var(--orange);
    display: flex; align-items: center; justify-content: center; gap: 14px;
    color: var(--navy-deep); font-weight: 700; font-size: 19px;
  }
  .contact-item { display: flex; align-items: center; gap: 6px; white-space: nowrap; }
  .contact-icon { width: 32px; height: 32px; flex: none; }
</style>
</head>
<body>
<main class="flyer">
  <svg class="backdrop" width="900" height="1200" viewBox="0 0 900 1200" aria-hidden="true">
    <defs>
      <linearGradient id="bandGrad" x1="0" y1="0" x2="1" y2="1">
        <stop offset="0" stop-color="#1a4d7a"/>
        <stop offset="1" stop-color="#123c62"/>
      </linearGradient>
    </defs>
    <rect width="900" height="1200" fill="#0d1726"/>
    <polygon points="0,0 272,0 0,366" fill="#133a5e"/>
    <polygon points="272,0 330,0 0,446 0,366" fill="#0f2c48"/>
    <polygon points="900,174 900,1132 199,1132" fill="url(#bandGrad)"/>
  </svg>

  <div class="brand">
    <span class="brand-mark"></span>
    <span class="brand-name">VUTEL</span>
  </div>
  <div class="brand-tagline">A LIGHT FOR EVERY LAND</div>

  <h1 class="title">
    <span class="title-line first">KESTREL</span>
    <span class="title-year">2019</span>
    <span class="title-line second">SUMMIT</span>
  </h1>
  <p class="topic">The Enemies of The End-Times Church</p>

  <svg class="speaker-photo" viewBox="0 0 400 430" role="img" aria-label="Photo of the speaker, Prophet Marcus Toliver, seated in a dark blazer and red sweater">
    <defs>
      <linearGradient id="photoGrad" x1="0" y1="0" x2="0" y2="1">
        <stop offset="0" stop-color="#4b4f55"/>
        <stop offset="1" stop-color="#2f3338"/>
      </linearGradient>
    </defs>
    <circle cx="191" cy="275" r="184" fill="#f7941d"/>
    <path d="M150 40 Q200 0 250 40 L262 150 Q340 170 362 240 L370 410 L40 410 L48 240 Q70 170 140 150 Z" fill="url(#photoGrad)"/>
  </svg>

  <div class="ribbon ribbon-role">Prophet</div>
  <div class="ribbon ribbon-name">Marcus Toliver</div>

  <section class="topics">
    <p class="topic-item">How the antichrist raises an army by social behavior engineering.</p>
    <p class="topic-item">How the architects of modern social constructs escaped the church's radar.</p>
    <p class="topic-item small">The Holy Spirit's end-times agenda:<span class="topic-punch">The Knock-Out Punch!</span></p>
  </section>

  <section class="event-info">
    <p class="event-dates">December 27, 28 &amp; 29</p>
    <p class="event-time">@ 6.00 pm</p>
    <p class="venue-name">Halvorn Community Center</p>
    <p class="venue-address">241 Pellham Street, Portland, ME 04102</p>
  </section>

  <footer class="contact-bar">
    <span class="contact-item">
      <svg class="contact-icon" viewBox="0 0 32 32" aria-hidden="true"><circle cx="16" cy="16" r="16" fill="#12253d"/><rect x="11" y="7" width="10" height="18" rx="2" fill="none" stroke="#f7941d" stroke-width="2"/><circle cx="16" cy="21.5" r="1.2" fill="#f7941d"/></svg>
      207-555-0148
    </span>
    <span class="contact-item">
      <svg class="contact-icon" viewBox="0 0 32 32" aria-hidden="true"><circle cx="16" cy="16" r="16" fill="#12253d"/><rect x="8" y="10" width="16" height="12" fill="none" stroke="#f7941d" stroke-width="2"/><path d="M8 10 L16 17 L24 10" fill="none" stroke="#f7941d" stroke-width="2"/></svg>
      contact@brookmeadow.example
    </span>
    <span class="contact-item">
      <svg class="contact-icon" viewBox="0 0 32 32" aria-hidden="true"><circle cx="16" cy="16" r="16" fill="#12253d"/><circle cx="16" cy="16" r="8.5" fill="none" stroke="#f7941d" stroke-width="1.8"/><ellipse cx="16" cy="16" rx="3.5" ry="8.5" fill="none" stroke="#f7941d" stroke-width="1.6"/><path d="M7.5 16 H24.5 M9 12 H23 M9 20 H23" stroke="#f7941d" stroke-width="1.4"/></svg>
      www.vutel.example
    </span>
  </footer>
</main>
</body>
</html>
```